M&A Advisory firm needs elegant and powerful letterhead

We need a powerful but elegant letterhead to engage with the international financial industry.

Target Market(s)

New York and International Financial Industry

Industry/Entity Type

Finance

Font styles to use
Other font styles liked:
• Poppins

Requirements
Must have
• 437 W 82nd Street 14th Floor New York, NY 10024 O: +1 (212) 555 0147 F: +1 (212) 555 0182

```html
<!DOCTYPE html>
<html lang="en">
<head>
<meta charset="utf-8">
<title>Meridane Letterhead</title>
<link rel="stylesheet" href="https://fonts.googleapis.com/css2?family=Open+Sans:wght@400;600;700&display=swap">
<style>
  :root {
    --brand-blue: #004b93;
    --accent-grey: #a7a7a9;
    --text-grey: #5a5a5c;
    --text-dark: #2b2b2d;
    --paper: #ffffff;
    --backdrop: #e9e9eb;
  }
  * { margin: 0; padding: 0; box-sizing: border-box; }
  html, body {
    width: 1200px; height: 795px; overflow: hidden;
    background: var(--backdrop);
    font-family: "Open Sans", sans-serif;
  }
  .letterhead {
    position: absolute; left: 333px; top: 20px;
    width: 534px; height: 755px;
    background: var(--paper);
    box-shadow: 0 2px 10px rgba(0,0,0,0.12);
    overflow: hidden;
  }
  .header-art, .footer-art { position: absolute; left: 0; width: 534px; }
  .header-art { top: 0; height: 130px; }
  .footer-art { bottom: 0; height: 40px; }
  .contact-phones {
    position: absolute; top: 28px; right: 30px;
    color: var(--paper); font-size: 7.5px; line-height: 11px;
  }
  .contact-phones li { list-style: none; display: flex; align-items: center; gap: 4px; }
  .icon { width: 8px; height: 8px; flex: none; }
  .brand {
    position: absolute; top: 120px; left: 44px;
    display: flex; align-items: center; gap: 8px;
  }
  .brand-dot { width: 14px; height: 14px; border-radius: 50%; background: var(--brand-blue); }
  .brand-name {
    font-size: 20px; font-weight: 400; letter-spacing: 1px;
    color: var(--brand-blue);
  }
  .letter {
    position: absolute; top: 182px; left: 68px; width: 380px;
    font-size: 8px; line-height: 11px; color: var(--text-dark);
  }
  .date { margin-bottom: 9px; }
  .recipient { margin-bottom: 9px; font-style: normal; }
  .salutation { font-weight: 700; font-size: 8.5px; margin-bottom: 12px; }
  .body-text p { color: var(--text-grey); margin-bottom: 11px; }
  .closing { margin-top: 18px; }
  .signature {
    width: 120px; height: 26px; margin: 4px 0;
    background: linear-gradient(90deg, rgba(0,75,147,0.18), rgba(0,75,147,0.05));
    border-radius: 3px;
  }
  .address {
    position: absolute; bottom: 28px; right: 30px;
    display: flex; align-items: center; gap: 5px;
    font-size: 7.5px; color: var(--text-dark);
  }
  .address .icon { width: 10px; height: 10px; }
</style>
</head>
<body>
  <main class="letterhead">
    <svg class="header-art" viewBox="0 0 534 130" aria-hidden="true">
      <path d="M150 0 L534 0 L534 70 C430 100 290 80 150 0 Z" fill="var(--brand-blue)"/>
      <path d="M534 58 C420 92 290 70 170 6" fill="none" stroke="var(--paper)" stroke-width="2.5"/>
      <path d="M0 112 C30 60 120 62 230 76 C350 92 450 95 534 78" fill="none" stroke="var(--accent-grey)" stroke-width="3"/>
    </svg>

    <ul class="contact-phones">
      <li>
        <svg class="icon" viewBox="0 0 10 10"><circle cx="5" cy="5" r="5" fill="#fff"/><path d="M3.2 2.4 L4.2 3.6 L3.7 4.3 C4.1 5.1 4.9 5.9 5.7 6.3 L6.4 5.8 L7.6 6.8 L7 7.7 C5 7.6 2.4 5 2.3 3 Z" fill="var(--brand-blue)"/></svg>
        +1 (212) 555 0147
      </li>
      <li>
        <svg class="icon" viewBox="0 0 10 10"><circle cx="5" cy="5" r="5" fill="#fff"/><rect x="2.6" y="3.4" width="4.8" height="3.4" fill="var(--brand-blue)"/><rect x="3.4" y="2.2" width="3.2" height="1.6" fill="var(--brand-blue)"/></svg>
        +1 (212) 555 0182
      </li>
    </ul>

    <div class="brand">
      <span class="brand-dot"></span>
      <span class="brand-name">MERIDANE</span>
    </div>

    <article class="letter">
      <p class="date">January 12, 2014</p>
      <address class="recipient">
        Mr. Alan Reyes<br>President<br>Harbor Corporation<br>111 Street Name, Suite#<br>City, State, 12345
      </address>
      <p class="salutation">Dear Mr. Alan,</p>
      <div class="body-text">
        <p>Lorem Ipsum is simply dummy text of the printing and typesetting industry. Lorem Ipsum has been the industry's standard dummy text ever since the 1500s, when an unknown printer took a galley of type and scrambled it to make a type specimen book. It has survived not only five centuries, but also the leap into electronic typesetting, remaining essentially unchanged.</p>
        <p>The standard chunk of Lorem Ipsum used since the 1500s is reproduced below for those interested. Sections 1.10.32 and 1.10.33 from the classic Latin source text are also reproduced in their exact original form, accompanied by English versions from a later printed translation.</p>
        <p>Lorem Ipsum is simply dummy text of the printing and typesetting industry. Lorem Ipsum has been the industry's standard dummy text ever since the 1500s, when an unknown printer took a galley of type and scrambled it to make a type specimen book. It has survived not only five centuries, but also the leap into electronic typesetting, remaining essentially unchanged. It was popularised in the</p>
      </div>
      <div class="closing">
        <p>Sincerely Your,</p>
        <div class="signature" role="img" aria-label="Handwritten signature"></div>
        <p>Name Last Name<br>Company Name</p>
      </div>
    </article>

    <div class="address">
      <svg class="icon" viewBox="0 0 10 10"><circle cx="5" cy="5" r="5" fill="var(--brand-blue)"/><path d="M5 2 C6.4 2 7.2 3 7.2 4.1 C7.2 5.4 5 8 5 8 C5 8 2.8 5.4 2.8 4.1 C2.8 3 3.6 2 5 2 Z" fill="#fff"/><circle cx="5" cy="4.1" r="0.9" fill="var(--brand-blue)"/></svg>
      437 W 82nd Street 14th Floor New York, NY 10024
    </div>

    <svg class="footer-art" viewBox="0 0 534 40" aria-hidden="true">
      <rect x="0" y="18" width="534" height="1.5" fill="var(--accent-grey)"/>
      <rect x="0" y="23" width="534" height="8" fill="var(--brand-blue)"/>
    </svg>
  </main>
</body>
</html>
```